Brightpagekit.com Website Design

We would like to redesign brightpagkit.com and we are looking for creative ideas. The new design should be clean and not resemble with any other existing website design.

The most important factor is that website have many banners/advertisements so the new design should be able to accommodate these banners of different size (Advertisement Friendly Design)

All Tools should be categorized under different main categories like all those tools that are related to content/writing will be shown under Content Tools ( Please find all categories and tools in attached file with the project). Right now all tools are showing randomly.

Also, Design single tool pages with sidebar, advertisement, and content placement.
ex. brightpagekit.com/plagiarism-checker/
brightpagekit.com/keyword-position/

Winning designer will also make the logo as well.

Target Market(s)

SEO Agencies, SEO executive, Article writers, Essay Writers, Plagiarism Checkers, Webmasters

Industry/Entity Type

Seo

Logo Text

Bright Page Kit

Number of Pages Required

5+ page

Font styles to use
Serif
Sans Serif
Other font styles liked:
• Any

Colors

Designer to choose colors to be used in the design.

Requirements
Must have
• 1) Clean Design
• 2) Modern Look
• 3) Easy To Navigate
• 4) Separate Icon for every Tool
• 5) Advertisement/Banners Freindly Design
Nice to have
• Matching Logo
• WOW Factor
Should not have
• Complex Design
• No drop down menu

```html
<!DOCTYPE html>
<html lang="en">
<head>
<meta charset="utf-8">
<title>Plagiarism Checker – Bright Page Kit</title>
<link href="https://fonts.googleapis.com/css2?family=Lato:wght@300;400;700&family=Merriweather:wght@400;700&display=swap" rel="stylesheet">
<style>
:root{
  --brand:#1b4f8c;
  --nav:#173e6c;
  --nav-active:#ffffff;
  --accent:#ef5a24;
  --ink:#2e3440;
  --muted:#59606b;
  --line:#e1e5ea;
  --soft:#f4f7fa;
  --ad-fill:#e9edf1;
  --ad-text:#9aa3ad;
  --tool:#12895a;
  --pill:#1f74d1;
}
*{box-sizing:border-box;margin:0;padding:0}
html,body{width:1200px;height:1200px;overflow:hidden;background:#fff}
body{position:relative;font-family:'Lato',sans-serif;color:var(--ink)}
.abs{position:absolute}
.serif{font-family:'Merriweather',serif}

/* header */
.top-rule{left:0;top:0;width:1200px;height:3px;background:var(--accent)}
.brand{left:120px;top:38px;display:flex;align-items:center;gap:10px}
.brand-mark{width:20px;height:20px;border-radius:4px;background:var(--accent)}
.brand-name{font-size:28px;font-weight:700;color:var(--brand);line-height:1}
.tagline{left:120px;top:80px;font-size:13px;color:var(--muted)}
.util-nav a{position:absolute;top:24px;font-size:13px;text-decoration:none;color:var(--ink);letter-spacing:.3px}
.util-nav a.hot{color:var(--accent)}
.util-nav a.pill{top:18px;left:951px;width:128px;height:27px;background:var(--pill);color:#fff;border-radius:14px;text-align:center;line-height:27px}
.search{left:822px;top:64px;width:257px;height:34px;border:1px solid var(--line);border-radius:17px;background:var(--soft)}
.search span{position:absolute;left:18px;top:9px;font-size:12.5px;color:#9aa1a9}
.search svg{position:absolute;left:228px;top:10px}

/* category navigation */
.main-nav{left:0;top:135px;width:1200px;height:57px;background:var(--nav)}
.main-nav a{position:absolute;top:0;height:57px;line-height:57px;color:#fff;font-size:15px;text-decoration:none}
.main-nav a.active{top:12px;height:33px;line-height:33px;left:120px;padding:0 16px;border-radius:17px;background:var(--nav-active);color:var(--nav);font-weight:700}

/* ads */
.ad-label{font-size:9px;color:#8a9099;text-align:center;letter-spacing:.5px;text-transform:uppercase}
.top-banner{left:207px;top:224px;width:776px;height:72px;border:1px solid var(--line);border-radius:8px;background:#fff;overflow:hidden}
.top-banner .pitch{position:absolute;left:36px;top:14px;font-size:19px;font-weight:300;color:#555;line-height:22px}
.top-banner .device{position:absolute;left:288px;top:0;width:186px;height:71px;background:#2b2b2b}
.top-banner .cover{position:absolute;left:312px;top:0;width:132px;height:71px;background:linear-gradient(#e8d56a,#7ea6c9)}
.top-banner .product{position:absolute;left:522px;top:18px;font-size:27px;font-weight:300;color:#555;letter-spacing:1px}
.top-banner .buy{position:absolute;left:667px;top:25px;width:73px;height:23px;border-radius:3px;background:var(--pill);color:#fff;font-size:10px;text-align:center;line-height:23px}
.side-ad{left:834px;top:329px;width:240px;height:200px;border:1px solid var(--line);border-radius:8px;background:#fff;overflow:hidden}
.side-ad .sky{height:80px;background:#4a8af4;position:relative}
.side-ad .band{height:43px;background:#1e5ad0;color:#fff;font-size:17px;font-weight:700;padding:12px 12px}
.side-ad .copy{position:absolute;left:12px;top:136px;width:150px;font-size:11px;line-height:13px;color:#111}
.side-ad .url{position:absolute;left:12px;top:182px;font-size:9px;color:#555}
.side-ad .go{position:absolute;left:185px;top:142px;width:41px;height:41px;border-radius:50%;background:#1e5ad0}
.leader{width:582px;height:71px;left:180px;border:1px dashed #c6cdd4;border-radius:8px;background:var(--ad-fill);color:var(--ad-text);font-size:38px;font-weight:300;text-align:center;line-height:69px}

/* tool content */
.page-title{left:120px;top:330px;width:701px;text-align:center;font-size:30px;font-weight:700;color:var(--brand)}
.page-title em{font-style:normal;color:var(--accent)}
.section-head{left:120px;top:392px;font-size:16px;font-weight:700;color:var(--ink)}
.intro{left:120px;top:419px;width:702px;font-size:12.5px;line-height:16px;color:var(--muted)}
.paste-head{left:120px;top:578px;font-size:20px;font-weight:400;color:var(--ink)}
.tabs span{position:absolute;top:630px;width:24px;height:22px;border:1px solid #c4cad1;border-radius:4px;font-size:11px;text-align:center;line-height:20px;color:#444}
.tabs span.on{background:var(--brand);border-color:var(--brand);color:#fff}
.tabs .hint{left:264px;top:634px;font-size:11px;color:var(--muted);border:none;width:auto;height:auto;line-height:14px}
.textbox{left:120px;top:656px;width:702px;height:205px;border:1px solid #b9c6d6;border-radius:8px;background:var(--soft);padding:10px 12px;font-size:12.5px;color:#7a828c}
.meta{font-size:11px;color:var(--muted)}
.meta b{color:var(--ink)}
.options{left:120px;top:892px;font-size:13px;color:var(--ink);font-weight:700}
.opt-link{font-size:13px;color:var(--accent);font-weight:700}
.opt-link i{font-style:normal;color:var(--ink);font-weight:400}
.no-file{left:120px;top:928px;font-size:13px;color:var(--muted)}
.btn{top:1058px;height:36px;font-size:15px;text-align:center;line-height:36px;border-radius:18px}
.btn-primary{left:313px;width:154px;background:var(--accent);color:#fff;font-weight:700}
.btn-outline{left:475px;width:154px;border:1px solid var(--accent);color:var(--ink);line-height:34px}
.privacy{left:120px;top:1143px;font-size:13px;font-weight:700;color:var(--ink);text-transform:uppercase;letter-spacing:.3px}
.privacy-note{left:120px;top:1162px;font-size:12.5px;color:var(--muted)}

/* sidebar */
.side-head{left:828px;top:565px;font-size:16px;font-weight:700;color:var(--brand)}
.side-head em{font-style:normal;color:var(--accent)}
.side-rule{left:828px;top:592px;width:241px;height:2px;background:var(--accent);opacity:.35}
.tool-list li{position:absolute;left:836px;width:200px;list-style:none;font-size:12.5px;color:var(--ink)}
.tool-icon{position:absolute;left:1045px;width:25px;height:25px;border-radius:6px;background:var(--tool);color:#fff;font-size:9px;font-weight:700;text-align:center;line-height:25px}
.tool-icon svg{margin-top:5px}
</style>
</head>
<body>
<div class="abs top-rule"></div>

<div class="abs brand"><span class="brand-mark"></span><span class="brand-name">Bright Page Kit</span></div>
<div class="abs tagline">Biggest Free SEO Tools Provider</div>

<nav class="util-nav">
  <a style="left:616px">ADVERTISE</a>
  <a style="left:722px">BLOG</a>
  <a class="hot" style="left:792px">LOGIN</a>
  <a class="hot" style="left:869px">REGISTER</a>
  <a class="pill">POPULAR TOOLS</a>
</nav>

<div class="abs search"><span>Search</span>
  <svg width="14" height="14" viewBox="0 0 14 14"><circle cx="6" cy="6" r="4.5" fill="none" stroke="#9aa1a9" stroke-width="1.5"/><line x1="9.3" y1="9.3" x2="13" y2="13" stroke="#9aa1a9" stroke-width="1.5"/></svg>
</div>

<nav class="abs main-nav">
  <a class="active">Content</a>
  <a style="left:213px">Images Handling</a>
  <a style="left:342px">Keywords</a>
  <a style="left:430px">BackLink</a>
  <a style="left:513px">Website Tracking</a>
  <a style="left:647px">Proxy</a>
  <a style="left:709px">Domains</a>
  <a style="left:790px">Meta</a>
  <a style="left:849px">Password</a>
  <a style="left:934px">PDF</a>
</nav>

<div class="abs ad-label" style="left:495px;top:209px;width:200px">Advertisements</div>
<div class="abs top-banner">
  <div class="pitch">The thin, light &amp; portable<br>tablet from Veltra.</div>
  <div class="device"></div>
  <div class="cover" role="img" aria-label="Book cover shown on tablet screen"></div>
  <div class="product">orbis 7</div>
  <div class="buy">Buy Now</div>
</div>

<div class="abs ad-label" style="left:854px;top:314px;width:200px">Advertisements</div>
<div class="abs side-ad">
  <div class="sky">
    <svg class="abs" style="left:18px;top:22px" width="34" height="34" viewBox="0 0 34 34"><path d="M3 10 L17 4 L31 10" fill="none" stroke="#fff" stroke-width="3"/><line x1="9" y1="14" x2="9" y2="32" stroke="#fff" stroke-width="3"/><line x1="25" y1="14" x2="25" y2="32" stroke="#fff" stroke-width="3"/></svg>
  </div>
  <div class="band">Book A Hotel Tonight</div>
  <div class="copy">Special Rates Until the End of the Month. No Booking Fees.</div>
  <div class="url">www.example.com</div>
  <div class="go"><svg width="41" height="41" viewBox="0 0 41 41"><path d="M17 12 L25 20.5 L17 29" fill="none" stroke="#fff" stroke-width="2.5"/></svg></div>
</div>

<h1 class="abs page-title serif">Plagiarism <em>Checker</em></h1>
<h2 class="abs section-head">Check For Plagiarism</h2>
<p class="abs intro">To use this plagiarism checker, please copy and paste your content in the box below, and then click on the big green button that says “Check Plagiarism!” then sit back and watch as your article is scanned for duplicated content.</p>

<div class="abs ad-label" style="left:371px;top:462px;width:200px">Advertisements</div>
<div class="abs leader" style="top:478px">728 x 90</div>

<h3 class="abs paste-head serif">Copy and paste your text below:</h3>
<div class="tabs">
  <span class="on" style="left:120px">1</span>
  <span style="left:148px">2</span>
  <span style="left:175px">3</span>
  <span style="left:202px">4</span>
  <span style="left:229px">5</span>
  <span class="hint">Select a sample text by clicking on the number</span>
</div>
<div class="abs textbox">Paste content here to check Plagiarism</div>

<div class="abs meta" style="left:120px;top:869px"><b>Limit:</b> 1000 Words per Search</div>
<div class="abs meta" style="left:721px;top:869px"><b>Total Words:</b> 0</div>

<div class="abs options">Advance options:</div>
<div class="abs opt-link" style="left:120px;top:909px">Upload a Document : <i>( .docx/.txt )</i></div>
<div class="abs opt-link" style="left:419px;top:909px">Exclude a specific URL :</div>
<div class="abs no-file">No File selected..</div>

<div class="abs ad-label" style="left:371px;top:954px;width:200px">Advertisements</div>
<div class="abs leader" style="top:970px">728 x 90</div>

<div class="abs btn btn-primary">Check Plagiarism</div>
<div class="abs btn btn-outline">Check Grammer</div>

<div class="abs privacy">✓ Your privacy, our priority</div>
<div class="abs privacy-note">Bright Page Kit are specifically designed to automatically delete any record of search/check made on them.</div>

<h3 class="abs side-head serif">Popular <em>SEO Tools</em></h3>
<div class="abs side-rule"></div>
<ol class="tool-list">
  <li style="top:602px">1. Plagiarism Checker</li>
  <li style="top:634px">2. Article Spinner / Rewriter</li>
  <li style="top:666px">3. Keyword Position Checker</li>
  <li style="top:698px">4. Grammar Checker</li>
  <li style="top:730px">5. Domain Authority Checker</li>
  <li style="top:762px">6. Page Rank Checker</li>
  <li style="top:794px">7. Image Compression Tool</li>
  <li style="top:826px">8. Reverse Image Search</li>
  <li style="top:858px">9. Page Authority checker</li>
  <li style="top:890px">10. Spell Checker</li>
  <li style="top:922px">11. Backlink Checker</li>
  <li style="top:954px">12. Traffic Rank Checker</li>
  <li style="top:986px">13. Backlink Maker</li>
  <li style="top:1018px">14. Domain Age Checker</li>
  <li style="top:1050px">15. Website Ping Tool</li>
  <li style="top:1082px">16. Website Seo Score Checker</li>
  <li style="top:1114px">17. Keyword Density Checker</li>
  <li style="top:1146px">18. Website Page Size Checker</li>
  <li style="top:1178px">19. Search Cache Checker</li>
</ol>

<div class="tool-icon" style="top:598px"><svg width="14" height="16" viewBox="0 0 14 16"><path d="M2 1h7l3 3v11H2z" fill="#fff"/></svg></div>
<div class="tool-icon" style="top:627px"><svg width="16" height="16" viewBox="0 0 16 16"><path d="M2 14 L4 10 L12 2 L14 4 L6 12 Z" fill="#fff"/></svg></div>
<div class="tool-icon" style="top:656px"><svg width="16" height="14" viewBox="0 0 16 14"><path d="M1 1v12h14" fill="none" stroke="#fff" stroke-width="1.5"/><path d="M3 10 L7 6 L9 8 L14 3" fill="none" stroke="#fff" stroke-width="1.5"/></svg></div>
<div class="tool-icon" style="top:685px;font-size:13px">A</div>
<div class="tool-icon" style="top:714px">DA</div>
<div class="tool-icon" style="top:742px">PR</div>
<div class="tool-icon" style="top:771px"><svg width="16" height="14" viewBox="0 0 16 14"><rect x="1" y="1" width="14" height="12" fill="none" stroke="#fff" stroke-width="1.5"/><line x1="4" y1="5" x2="12" y2="5" stroke="#fff"/><line x1="4" y1="9" x2="12" y2="9" stroke="#fff"/></svg></div>
<div class="tool-icon" style="top:800px"><svg width="16" height="14" viewBox="0 0 16 14"><rect x="1" y="1" width="14" height="12" fill="none" stroke="#fff" stroke-width="1.5"/><path d="M2 12 L6 7 L9 10 L11 8 L14 12Z" fill="#fff"/></svg></div>
<div class="tool-icon" style="top:829px">PA</div>
<div class="tool-icon" style="top:858px;font-size:7px">ABC</div>
<div class="tool-icon" style="top:886px"><svg width="16" height="16" viewBox="0 0 16 16"><path d="M6 10 L10 6 M5 8 L3 10 a2.5 2.5 0 0 0 3.5 3.5 L8 11 M11 8 L13 6 a2.5 2.5 0 0 0 -3.5 -3.5 L8 5" fill="none" stroke="#fff" stroke-width="1.6"/></svg></div>
<div class="tool-icon" style="top:915px"><svg width="16" height="14" viewBox="0 0 16 14"><path d="M1 1v12h14" fill="none" stroke="#fff" stroke-width="1.5"/><path d="M3 11 L6 5 L9 8 L14 3 V11Z" fill="#fff"/></svg></div>
<div class="tool-icon" style="top:944px"><svg width="16" height="16" viewBox="0 0 16 16"><circle cx="5" cy="5" r="3" fill="none" stroke="#fff" stroke-width="1.6"/><circle cx="11" cy="11" r="3" fill="none" stroke="#fff" stroke-width="1.6"/></svg></div>
<div class="tool-icon" style="top:973px"><svg width="16" height="16" viewBox="0 0 16 16"><path d="M3 8 a5 5 0 1 0 2 -4" fill="none" stroke="#fff" stroke-width="1.8"/><path d="M8 5 V8 L10 10" fill="none" stroke="#fff" stroke-width="1.6"/></svg></div>
<div class="tool-icon" style="top:1002px"><svg width="14" height="14" viewBox="0 0 14 14"><circle cx="2.5" cy="11.5" r="2" fill="#fff"/><path d="M1 6 a7 7 0 0 1 7 7 M1 1 a12 12 0 0 1 12 12" fill="none" stroke="#fff" stroke-width="1.8"/></svg></div>
<div class="tool-icon" style="top:1030px"><svg width="14" height="16" viewBox="0 0 14 16"><rect x="1" y="1" width="12" height="14" fill="none" stroke="#fff" stroke-width="1.5"/><path d="M3 6h8M3 9h8M3 12h8M5.5 4v10M8.5 4v10" stroke="#fff"/></svg></div>
<div class="tool-icon" style="top:1059px"><svg width="14" height="16" viewBox="0 0 14 16"><path d="M2 1h7l3 3v11H2z" fill="none" stroke="#fff" stroke-width="1.5"/><path d="M4 8h6M4 11h6" stroke="#fff"/></svg></div>
<div class="tool-icon" style="top:1088px"><svg width="16" height="16" viewBox="0 0 16 16"><path d="M8 2v12M4 14h8M2 5h12M2 5 L0.5 10 h3Z M14 5 L12.5 10 h3Z" fill="none" stroke="#fff" stroke-width="1.3"/></svg></div>
<div class="tool-icon" style="top:1117px"><svg width="16" height="16" viewBox="0 0 16 16"><path d="M3 8 a5 5 0 1 0 2 -4" fill="none" stroke="#fff" stroke-width="2"/><path d="M2 2 V6 H6" fill="none" stroke="#fff" stroke-width="1.8"/></svg></div>
<div class="tool-icon" style="top:1146px;font-size:8px">MZ</div>
</body>
</html>
```